Movie poster for short film: TINDERLOCK

We need a creative, artistic, stylized poster design for our short film TINDERLOCK. We would like to see designs with graphics and bold colors more than photographs. The photographs we are posting are more for reference- you do not have to use them in the poster! We are looking for something clean and simple. The film is a drama so please don't make it funny. The mood of the film is thoughtful and introspective. Name of film should be in all caps. Things to include in the poster:
Name of film: TINDERLOCK
Lantern Hollow Productions
Starring Marisa Kovalenko

Here is a brief plot synopsis: TINDERLOCK follows one night in the life of a rebellious young woman who breaks into a diner after hours with a can of spray paint. Her intentions change after she ends up discovering what's left of a love story.

The movie is somewhat experimental, set to music for part of it with no dialog. The whole movie takes place in an old fashioned diner.

Target Market(s)

Film festival attendees between the ages of 20-50

Industry/Entity Type

Movie

Font styles to use
Sans Serif

Requirements
Must have
• See project description above- also the film is somewhat dark in nature so please don't make it too 'happy' looking.

```html
<!DOCTYPE html>
<html lang="en">
<head>
<meta charset="utf-8">
<title>TINDERLOCK — Poster</title>
<link rel="stylesheet" href="https://fonts.googleapis.com/css2?family=Montserrat:wght@700&family=Oswald:wght@400;600&display=swap">
<style>
  :root {
    --ink: #000000;
    --paper: #ffffff;
    --candy-red: #d8242c;
    --candy-pink: #ec7fa6;
    --candy-blue: #2e9fd6;
    --candy-navy: #233a9c;
    --candy-yellow: #e6e43a;
    --candy-orange: #f2a12c;
    --candy-green: #3cb64a;
    --candy-white: #f1efe9;
  }
  html, body {
    margin: 0;
    padding: 0;
    width: 800px;
    height: 1200px;
    overflow: hidden;
    background: var(--ink);
  }
  .poster {
    position: relative;
    width: 800px;
    height: 1200px;
    background: var(--ink);
    color: var(--paper);
    overflow: hidden;
  }
  .studio {
    position: absolute;
    top: 62px;
    left: 0;
    width: 100%;
    text-align: center;
    font-family: "Oswald", sans-serif;
    font-size: 23px;
    letter-spacing: 0.3px;
    text-transform: uppercase;
    margin: 0;
  }
  .studio strong { font-weight: 600; }
  .studio span { font-weight: 400; }
  .title {
    position: absolute;
    top: 128px;
    left: 0;
    width: 100%;
    text-align: center;
    font-family: "Montserrat", sans-serif;
    font-weight: 700;
    font-size: 96px;
    line-height: 1;
    letter-spacing: 1px;
    margin: 0;
  }
  .billing {
    position: absolute;
    top: 240px;
    left: 0;
    width: 100%;
    text-align: center;
    font-family: "Oswald", sans-serif;
    font-size: 27px;
    text-transform: uppercase;
    margin: 0;
  }
  .billing span { font-weight: 400; }
  .billing strong { font-weight: 600; }
  .portrait {
    position: absolute;
    left: 125px;
    top: 418px;
    width: 565px;
    height: 782px;
    border-radius: 46% 46% 0 0 / 30% 30% 0 0;
    background:
      radial-gradient(circle at 25% 20%, var(--candy-pink) 0, transparent 40%),
      radial-gradient(circle at 75% 30%, var(--candy-blue) 0, transparent 38%),
      radial-gradient(circle at 40% 60%, var(--candy-yellow) 0, transparent 35%),
      radial-gradient(circle at 70% 80%, var(--candy-green) 0, transparent 35%),
      radial-gradient(circle at 20% 85%, var(--candy-orange) 0, transparent 35%),
      linear-gradient(160deg, var(--candy-red), var(--candy-navy));
  }
</style>
</head>
<body>
  <main class="poster">
    <p class="studio"><strong>Lantern Hollow</strong> <span>Productions</span></p>
    <h1 class="title">TINDERLOCK</h1>
    <p class="billing"><span>Starring</span> <strong>Marisa Kovalenko</strong></p>
    <div class="portrait" role="img" aria-label="Side-profile silhouette of a young woman filled with brightly coloured candy balls"></div>
  </main>
</body>
</html>
```